Dental Business Card

I need Dental oriented business cards.
On the front side -
- on the first line, my name:
Dr Marlow Tasker
- on the second line (just underneath):
Doctor of Dental Medicine
- on the third line, or underneath that or in a corner, I would like the address and phone number:
5192 Ch. Birchfield
Montreal QC H2P 4K8
514-629-5074
- other than that i would maybe like a logo of a tooth, but i want it to be subtle and very basic!
- I would like the card to be preferably black or dark grey-ish with the writing in white
On the other side -
- 2-3 lines with the possibility to write the next appointment the box with the lines should be white, with the rest of the card being black

```html
<!DOCTYPE html>
<html lang="en">
<head>
<meta charset="utf-8">
<title>Dr Marlow Tasker – Business Card</title>
<link href="https://fonts.googleapis.com/css2?family=Questrial&family=Nunito:wght@700&display=swap" rel="stylesheet">
<style>
  :root {
    --backdrop: #262626;
    --card: #181818;
    --ink: #f2f2f2;
    --ink-soft: #d4d4d4;
    --field: #e6e6e6;
  }
  html, body {
    margin: 0;
    width: 1200px;
    height: 1200px;
    overflow: hidden;
    background: var(--backdrop);
  }
  .canvas {
    position: relative;
    width: 1200px;
    height: 1200px;
  }
  .card {
    position: absolute;
    top: 226px;
    width: 424px;
    height: 746px;
    background: var(--card);
    box-shadow: 0 6px 24px rgba(0,0,0,.55);
    color: var(--ink);
    font-family: "Questrial", sans-serif;
    text-align: center;
  }
  .card--front { left: 136px; }
  .card--back { left: 640px; }

  .brand-mark {
    position: absolute;
    left: 131px;
    top: 250px;
    width: 164px;
    height: 164px;
    box-sizing: border-box;
    border: 3px solid var(--ink);
    border-radius: 50%;
    display: flex;
    align-items: center;
    justify-content: center;
    font-size: 18px;
    line-height: 1.2;
    color: var(--ink);
  }
  .doctor-name {
    position: absolute;
    left: 0; right: 0;
    top: 440px;
    margin: 0;
    font-family: "Nunito", sans-serif;
    font-weight: 700;
    font-size: 26px;
    letter-spacing: .3px;
  }
  .doctor-title {
    position: absolute;
    left: 0; right: 0;
    top: 478px;
    margin: 0;
    font-size: 19px;
    letter-spacing: .6px;
    color: var(--ink-soft);
  }

  .appointment-heading {
    position: absolute;
    left: 0; right: 0;
    top: 90px;
    margin: 0;
    font-weight: 400;
    font-size: 26px;
    letter-spacing: .8px;
  }
  .appointment-field {
    position: absolute;
    left: 53px;
    width: 318px;
    height: 46px;
    background: var(--field);
  }
  .appointment-field:nth-of-type(1) { top: 172px; }
  .appointment-field:nth-of-type(2) { top: 233px; }
  .appointment-field:nth-of-type(3) { top: 293px; }

  .cancellation-note {
    position: absolute;
    left: 40px; right: 40px;
    top: 384px;
    margin: 0;
    font-size: 20px;
    line-height: 25px;
    color: var(--ink-soft);
  }
  .contact {
    position: absolute;
    left: 0; right: 0;
    top: 557px;
    margin: 0;
    font-style: normal;
    font-size: 19px;
    line-height: 25px;
    color: var(--ink-soft);
  }
  .contact-phone { display: block; margin-top: 25px; }
</style>
</head>
<body>
<main class="canvas">
  <section class="card card--front">
    <div class="brand-mark">Tasker<br>Dental</div>
    <h1 class="doctor-name">Dr Marlow Tasker</h1>
    <p class="doctor-title">Doctor of Dental Medicine</p>
  </section>

  <section class="card card--back">
    <h2 class="appointment-heading">Next Appointment</h2>
    <div class="appointment-field"></div>
    <div class="appointment-field"></div>
    <div class="appointment-field"></div>
    <p class="cancellation-note">We value your time and that of other guests and a 24 hr notice is required if you are not able to keep your appointment</p>
    <address class="contact">
      5192 Ch. Birchfield<br>
      Montreal QC H2P 4K8
      <span class="contact-phone">514-629-5074</span>
    </address>
  </section>
</main>
</body>
</html>
```